Business Card Design Project

TRX Solutions is a Electrical and Communications Services and Maintenance contractor to the Mining Oil and Gas sectors of Australia.
Our clients will be planners, Schedulers, Tradespeople and Engineers

We are yet to determine the primary colours that we will use on the business cards but the logos attached will form foundation of the colours used for logos on Business cards, Website, Uniforms, vehicles etc.

Target Market(s)

Mining engineers and shedulers

Industry/Entity Type

Contractor

Requirements
Must have
• information to be included on the card

Name: Derek Hanley
Title: Managing Director
Company: TRX Solutions Pty Ltd
Phone: 08 9XXX XXXX
Mobile 0400 318 942
email: dhanley@trxsolutionsgroup.com.au
Website www.trxsolutionsgroup.com.au

Address: U5/14 Kettering Street Kelmore, WA 6123
Postal Address: PO Box 7183 Kelmore WA 6124

Nice to have
• Double sided. Maybe the logo on the back

```html
<!DOCTYPE html>
<html lang="en">
<head>
<meta charset="utf-8">
<title>TRX Solutions – Business Card</title>
<link href="https://fonts.googleapis.com/css2?family=Arimo:ital,wght@0,400;0,700;1,700&family=Questrial&display=swap" rel="stylesheet">
<style>
  :root {
    --bg: #e9e6e1;
    --navy: #1b2a4c;
    --navy-deep: #121c3a;
    --steel: #8d92a6;
    --accent: #f05a24;
    --ink: #222;
    --white: #fff;
  }
  * { margin: 0; padding: 0; box-sizing: border-box; }
  html, body { width: 1200px; height: 867px; overflow: hidden; background: var(--bg); }
  .canvas { position: relative; width: 1200px; height: 867px; }
  .card {
    position: absolute; width: 606px; height: 345px; background: var(--white);
    overflow: hidden; box-shadow: 0 4px 14px rgba(0,0,0,.25);
  }
  .card-front { left: 358px; top: 55px; }
  .card-back { left: 161px; top: 464px; }
  .card svg.waves { position: absolute; inset: 0; width: 100%; height: 100%; }

  .brand {
    position: absolute; display: flex; align-items: center; gap: 12px;
    font-family: "Questrial", sans-serif; color: var(--navy); white-space: nowrap;
  }
  .card-front .brand { left: 0; right: 0; top: 130px; justify-content: center; font-size: 50px; }
  .card-back .brand { left: 52px; top: 24px; font-size: 34px; gap: 8px; }
  .brand-mark { width: 14px; height: 14px; background: var(--accent); }
  .card-back .brand-mark { width: 10px; height: 10px; }

  .company {
    position: absolute; left: 55px; top: 100px;
    font-family: "Arimo", sans-serif; font-weight: 700; font-size: 17px; color: var(--navy);
  }
  .person { position: absolute; right: 36px; top: 64px; text-align: right; font-family: "Arimo", sans-serif; }
  .person-name { font-weight: 700; font-style: italic; font-size: 16px; color: var(--navy); }
  .person-title { font-size: 13px; color: var(--ink); margin-top: 3px; }

  .edge-tab { position: absolute; left: 0; top: 145px; width: 6px; height: 94px; background: var(--navy); border-radius: 0 4px 4px 0; }

  .contacts { position: absolute; left: 30px; top: 141px; list-style: none; font-family: "Arimo", sans-serif; font-size: 14px; color: var(--ink); }
  .contacts li { display: flex; align-items: center; height: 19.6px; white-space: nowrap; }
  .contacts .icon { width: 14px; height: 14px; margin-right: 7px; flex: none; }
  .contacts .no-icon { padding-left: 21px; }
</style>
</head>
<body>
<main class="canvas">

  <section class="card card-front" aria-label="Card front">
    <svg class="waves" viewBox="0 0 606 345" preserveAspectRatio="none" aria-hidden="true">
      <defs>
        <linearGradient id="bandFront" x1="0" x2="1" y1="0" y2="0">
          <stop offset="0" stop-color="#1b2447"/>
          <stop offset=".3" stop-color="#8a8fa3"/>
          <stop offset=".5" stop-color="#1d2a4d"/>
          <stop offset=".72" stop-color="#a3a6b4"/>
          <stop offset="1" stop-color="#141d3d"/>
        </linearGradient>
      </defs>
      <rect width="606" height="345" fill="url(#bandFront)"/>
      <path d="M0,94 C200,112 380,34 606,36" fill="none" stroke="#121c3a" stroke-width="5"/>
      <path d="M0,292 C200,312 400,238 606,240" fill="none" stroke="#121c3a" stroke-width="6"/>
      <path d="M0,100 C200,118 380,42 606,44 L606,234 C400,232 200,306 0,286 Z" fill="#fff"/>
      <path d="M200,290 C360,268 480,236 606,248" fill="none" stroke="#fff" stroke-width="3"/>
    </svg>
    <div class="brand"><span class="brand-name">TRX Solutions</span><span class="brand-mark"></span></div>
  </section>

  <section class="card card-back" aria-label="Card back">
    <svg class="waves" viewBox="0 0 606 345" preserveAspectRatio="none" aria-hidden="true">
      <defs>
        <linearGradient id="bandBack" x1="0" x2="1" y1="0" y2="0">
          <stop offset="0" stop-color="#9a9eae"/>
          <stop offset=".3" stop-color="#1b2a4c"/>
          <stop offset=".55" stop-color="#8d92a6"/>
          <stop offset=".8" stop-color="#2a3658"/>
          <stop offset="1" stop-color="#121c3a"/>
        </linearGradient>
      </defs>
      <path d="M0,292 C200,304 400,236 606,236 L606,345 L0,345 Z" fill="url(#bandBack)"/>
      <path d="M300,266 C430,244 520,230 606,228" fill="none" stroke="#121c3a" stroke-width="5"/>
      <path d="M0,297 C200,309 400,241 606,241 L606,247 C400,247 200,317 0,305 Z" fill="#fff"/>
    </svg>

    <div class="brand"><span class="brand-name">TRX Solutions</span><span class="brand-mark"></span></div>
    <p class="company">TRX Solutions Pty Ltd</p>

    <div class="person">
      <p class="person-name">Derek Hanley</p>
      <p class="person-title">Managing Director</p>
    </div>

    <span class="edge-tab"></span>

    <ul class="contacts">
      <li><svg class="icon" viewBox="0 0 14 14"><circle cx="7" cy="7" r="6" fill="none" stroke="#1b2a4c" stroke-width="1.4"/><path d="M5,4 h2 v6 h-2" fill="none" stroke="#1b2a4c" stroke-width="1.4"/></svg>08 9XXX XXXX</li>
      <li><svg class="icon" viewBox="0 0 14 14"><rect x="4" y="1.5" width="6" height="11" rx="1.2" fill="none" stroke="#1b2a4c" stroke-width="1.4"/><rect x="5.5" y="3.5" width="3" height="3" fill="#1b2a4c"/></svg>0400 318 942</li>
      <li><svg class="icon" viewBox="0 0 14 14"><rect x="1" y="3" width="12" height="8" fill="none" stroke="#1b2a4c" stroke-width="1.3"/><path d="M1,3 L7,8 L13,3" fill="none" stroke="#1b2a4c" stroke-width="1.3"/></svg>dhanley@trxsolutionsgroup.com.au</li>
      <li><svg class="icon" viewBox="0 0 14 14"><circle cx="7" cy="7" r="6" fill="none" stroke="#1b2a4c" stroke-width="1.3"/><ellipse cx="7" cy="7" rx="2.6" ry="6" fill="none" stroke="#1b2a4c" stroke-width="1.1"/><path d="M1,7 h12" stroke="#1b2a4c" stroke-width="1.1"/></svg>www.trxsolutionsgroup.com.au</li>
      <li><svg class="icon" viewBox="0 0 14 14"><path d="M1,7 L7,1.5 L13,7 M3,6 V13 H11 V6" fill="none" stroke="#1b2a4c" stroke-width="1.4"/><rect x="6" y="9" width="2" height="4" fill="#1b2a4c"/></svg>U5/14 Kettering Street Kelmore, WA 6123</li>
      <li class="no-icon">PO Box 7183 Kelmore WA 6124</li>
    </ul>
  </section>

</main>
</body>
</html>
```